Tarnel-Holdings. Limestone; improving the world

New Limestone company and need logo design.
Limestone offsets carbon mitigation industries restore and replenish soil fertilities in the Prairies, the breadbasket of the world. At the same time, Limestone is proving a critical emergent component of carbon capture sequestration technology will therefore play a critical role in the development of the western Canadian energy industries
Our limestone resources are situated in the foothills of the Canadian Rockies well-positioned above the sprawling fields of the vast peace district.
Target Market(s)
Agriculture and oli sites
Logo Text
Tarnel Holdings
Number of Pages Required
3 page

```html
<!DOCTYPE html>
<html lang="en">
<head>
<meta charset="utf-8">
<title>Tarnel Holdings</title>
<link rel="stylesheet" href="https://fonts.googleapis.com/css2?family=Gelasio:wght@400;700&family=Mulish:wght@500&display=swap">
<style>
  :root {
    --ink: #33271f;
    --text: #2f2a27;
    --white: #ffffff;
    --green: #5cbf3f;
    --footer-bg: #f5f5f5;
    --hero-top: #e9e3b0;
    --hero-mid: #9a9a55;
    --hero-low: #4d5631;
    --field-sky: #2f7891;
    --field-glow: #d9a261;
    --field-crop: #a87523;
    --field-dark: #5a3e14;
  }
  * { margin: 0; padding: 0; box-sizing: border-box; }
  html, body { width: 740px; height: 1200px; overflow: hidden; background: var(--white); }
  body { position: relative; font-family: "Gelasio", "Palatino Linotype", serif; color: var(--text); }

  .site-header { position: absolute; left: 0; top: 0; width: 740px; height: 55px; }
  .brand { position: absolute; left: 61px; top: 15px; display: flex; align-items: center; gap: 7px; }
  .brand-mark { width: 16px; height: 16px; background: var(--ink); }
  .brand-name { font-size: 17px; color: var(--ink); font-weight: 400; line-height: 1; }
  .main-nav a { position: absolute; top: 26px; font-size: 9.5px; color: var(--text); text-decoration: none; }
  .main-nav .active { font-weight: 700; }

  .hero { position: absolute; left: 0; top: 55px; width: 740px; height: 317px;
    background: linear-gradient(200deg, var(--hero-top) 0%, #c9bb6d 30%, var(--hero-mid) 55%, var(--hero-low) 100%); }
  .hero-title { position: absolute; left: 40px; right: 40px; top: 246px; text-align: center;
    font-family: "Mulish", Arial, sans-serif; font-weight: 500; font-size: 18.5px; line-height: 29.5px; color: var(--white); }

  .mission { position: absolute; left: 62px; top: 411px; width: 320px; font-size: 18px; line-height: 27px; color: var(--text); }
  .info { position: absolute; left: 412px; width: 270px; }
  .info h2 { font-weight: 400; font-size: 17px; line-height: 22px; margin-bottom: 4px; color: var(--text); }
  .info p { font-size: 10px; line-height: 17px; color: var(--text); }
  .info-about { top: 413px; }
  .info-special { top: 539px; }

  .feature { position: absolute; left: 61px; top: 676px; width: 618px; height: 268px;
    background: linear-gradient(180deg, var(--field-sky) 0%, #9fa6a0 22%, var(--field-glow) 45%, var(--field-crop) 68%, var(--field-dark) 100%); }
  .feature-card { position: absolute; left: 12px; top: 51px; width: 253px; height: 164px;
    background: rgba(240, 240, 240, 0.88); border-left: 3px solid var(--green); padding: 24px 16px 0 9px; }
  .feature-card h2 { font-weight: 400; font-size: 17px; line-height: 22px; margin-bottom: 5px; }
  .feature-card p { font-size: 10px; line-height: 17px; }

  .site-footer { position: absolute; left: 0; top: 1020px; width: 740px; height: 147px; background: var(--footer-bg); }
  .footer-company { position: absolute; left: 62px; top: 24px; font-size: 11.5px; font-weight: 700; }
  .footer-address { position: absolute; left: 62px; top: 46px; font-size: 10px; line-height: 15px; }
  .footer-contact { position: absolute; left: 62px; top: 101px; font-size: 10px; line-height: 15px; }
  .footer-nav { position: absolute; left: 413px; top: 25px; list-style: none; }
  .footer-nav li { font-size: 9.5px; line-height: 18.7px; }
  .footer-nav .active { font-weight: 700; }

  .copyright { position: absolute; left: 0; top: 1167px; width: 740px; height: 33px; background: var(--ink);
    color: var(--white); font-size: 9.5px; text-align: center; line-height: 33px; }
</style>
</head>
<body>
  <header class="site-header">
    <div class="brand">
      <span class="brand-mark"></span>
      <span class="brand-name">Tarnel Holdings</span>
    </div>
    <nav class="main-nav">
      <a class="active" href="#" style="left:440px">Home</a>
      <a href="#" style="left:500px">About Us</a>
      <a href="#" style="left:573px">FAQs</a>
      <a href="#" style="left:631px">Contact Us</a>
    </nav>
  </header>

  <section class="hero" role="img" aria-label="Aerial photo of a truck on a highway beside a warehouse and sunlit prairie fields">
    <p class="hero-title">Limestone Offsets Carbon Mitigation Industries Restore And Replenish Soil Fertilities In The Prairies, The Breadbasket of The World.</p>
  </section>

  <p class="mission">Our Mission&nbsp; Is to Improve our world by responsibly meeting society’s needs for quality lime and limestone products.</p>

  <div class="info info-about">
    <h2>About Us</h2>
    <p>Lorem ipsum dolor sit amet, consectetuer adpiscing elit, sed diam nonummy nibh euismod tincidunt ut laoreet dolore magna aliquam erat volutpat. Ut wisi enim ad minim veniam, quis nostrud exerci tatiofdn ullamcorper suscipit lobortis nisl ut aliquip commodo.</p>
  </div>
  <div class="info info-special">
    <h2>Special Opportunities</h2>
    <p>Our limestone resources are situated in the foothills of the Canadian Rockies well-positioned above the sprawling fields of the vast peace district.</p>
  </div>

  <section class="feature" role="img" aria-label="Photo of a golden wheat field at sunset with a tree line on the horizon">
    <div class="feature-card">
      <h2>Sustainability</h2>
      <p>Lorem ipsum dolor sit amet, contetr adpiscing elit, sed diam nonummy nibh eumod tincidunt ut laoreet dolore magna aliquam erat volutpat. Ut wisi enim ad minim veniam, quis nostrud exerci tatiofdn ullamcorper.</p>
    </div>
  </section>

  <footer class="site-footer">
    <p class="footer-company">Tarnel-Holdings Management, LLC</p>
    <p class="footer-address">88 Calder Ridge Rd, Suite 4<br>Fairhaven, AB T0H 2K0</p>
    <p class="footer-contact">For any inquiries, please contact<br>mara@tarnelholdings.example</p>
    <ul class="footer-nav">
      <li class="active">Home</li>
      <li>About Us</li>
      <li>FAQs</li>
      <li>Contact Us</li>
    </ul>
  </footer>
  <div class="copyright">Copyright © 2021 Tarnel-Holdings.&nbsp; All Right Reserved.</div>
</body>
</html>
```